Design & Build a Website with Wordpress for an international consulting company. Please read the details in the attached carefully.

I will be pleased to answer any questions you may have.

Thank you.

Thank you.

Thank you.
Updates

Hi, the home page shall have a placement for newsletter signup too. Thank you. Added Wednesday, March 9, 2016

Target Market(s)

US EU

Industry/Entity Type

Business Consultant

Font styles to use
Sans Serif

Requirements
Must have
• Coinvale portal, wordpress, responsive, accommodating the logo (download from the current site).
Nice to have
• professional, simple and elegant design

```html
<!DOCTYPE html>
<html lang="en">
<head>
<meta charset="utf-8">
<title>Meridane – Help East and West Transact</title>
<link href="https://fonts.googleapis.com/css2?family=Oswald:wght@300;400;500&family=Open+Sans:wght@400;600&display=swap" rel="stylesheet">
<style>
:root{
  --red:#ea3345;
  --red-dark:#d8293b;
  --ink:#333;
  --muted:#666;
  --line:#ddd;
  --black:#050505;
  --panel:#3a3a3a;
  --white:#fff;
}
*{box-sizing:border-box;margin:0;padding:0}
html,body{width:738px;height:1200px;overflow:hidden}
body{position:relative;background:var(--white);font-family:"Open Sans",Arial,sans-serif;color:var(--ink)}
.abs{position:absolute}
.heading{font-family:"Oswald",Arial,sans-serif;font-weight:300;color:var(--red)}
.section-title{position:absolute;left:153px;font-family:"Oswald",Arial,sans-serif;font-weight:300;color:var(--red);font-size:22px;line-height:1;display:flex;align-items:flex-end}
.section-title::after{content:"";display:block;height:1px;background:var(--line);margin-left:6px;margin-bottom:4px}
.t-why::after{width:150px}.t-services::after{width:150px}.t-products::after{width:160px}.t-blog::after{width:160px}

.topbar{left:0;top:0;width:738px;height:12px;background:var(--red);color:#fff;font-size:5px;line-height:12px}
.topbar .note{position:absolute;left:153px}
.topbar .account{position:absolute;left:535px;display:flex;gap:12px;font-family:"Oswald",sans-serif;font-size:6px}

.header{left:0;top:12px;width:738px;height:44px;background:#fff}
.brand{position:absolute;left:157px;top:11px;display:flex;align-items:center;gap:4px}
.brand .mark{width:10px;height:10px;border-radius:50%;background:var(--red)}
.brand .name{font-family:"Oswald",sans-serif;font-weight:500;font-size:17px;color:var(--red);letter-spacing:.5px}
.brand-tag{position:absolute;left:202px;top:32px;font-size:4.5px;color:var(--red)}
.nav{position:absolute;left:311px;top:26px;display:flex;gap:11px;font-family:"Oswald",sans-serif;font-size:7.5px;color:#333}
.nav .active{color:var(--red);border-bottom:1px solid var(--red);padding-bottom:2px}
.social{position:absolute;left:547px;top:28px;display:flex;gap:5px}
.social span{width:5px;height:5px;border-radius:50%;background:var(--red)}

.hero{left:0;top:56px;width:738px;height:223px;background:linear-gradient(90deg,#e9ecec 0%,#f3f4f3 30%,#d7cfc6 55%,#bfc6ce 70%,#eef1f2 100%)}
.hero-panel{left:154px;top:131px;width:184px;height:85px;background:var(--panel);border-bottom:3px solid var(--red);color:#fff;padding:8px 5px}
.hero-panel h2{font-family:"Oswald",sans-serif;font-weight:400;font-size:11px;margin-bottom:5px}
.hero-panel ul{list-style:none;display:grid;grid-template-columns:84px 90px;row-gap:3px;font-family:"Oswald",sans-serif;font-weight:300;font-size:7.5px;color:var(--red);padding-left:9px}

.why-list{left:160px;top:320px;list-style:none;font-family:"Oswald",sans-serif;font-weight:300;font-size:6.4px;color:#444}
.why-list li{margin-bottom:4px;display:flex;align-items:center;gap:4px}
.why-list li::before{content:"";width:2px;height:2px;border:1px solid var(--red);border-radius:50%}
.why-art{left:408px;top:287px}

.card{position:absolute;top:417px;height:174px;overflow:hidden}
.card .photo{position:absolute;inset:0}
.card .label{position:absolute;left:0;bottom:0;width:100%;height:29px;background:var(--red);color:#fff;font-family:"Oswald",sans-serif;font-size:15px;display:flex;align-items:center;justify-content:center;gap:6px}
.card.featured{background:var(--red);color:#fff;text-align:center;padding-top:51px}
.card.featured h3{font-family:"Oswald",sans-serif;font-weight:400;font-size:15px;display:flex;justify-content:center;gap:5px;align-items:center}
.card.featured p{font-size:7px;line-height:10px;margin:18px 18px 0}

.order{left:0;top:605px;width:738px;height:150px;background:linear-gradient(90deg,#2a2623 0%,#3d3732 45%,#302b27 75%,#1f1c1a 100%)}
.order h2{position:absolute;left:266px;top:12px;width:207px;text-align:center;font-family:"Oswald",sans-serif;font-weight:300;font-size:19px;color:var(--red);border-bottom:1px solid #888;padding-bottom:3px}
.field{position:absolute;border-bottom:1px solid #ccc;color:#eee;font-size:4.5px;padding-bottom:2px}
.field.select::after{content:"";position:absolute;right:2px;top:1px;width:3px;height:3px;border-right:1px solid #eee;border-bottom:1px solid #eee;transform:rotate(45deg)}
.send-btn{position:absolute;left:333px;top:115px;width:72px;height:15px;border:1.5px solid var(--red);border-radius:8px;color:#fff;font-family:"Oswald",sans-serif;font-size:8px;text-align:center;line-height:12px}

.product{position:absolute;top:791px;width:142px;height:97px;overflow:hidden}
.product .label{position:absolute;left:0;bottom:0;width:100%;height:17px;background:var(--red);color:#fff;font-family:"Oswald",sans-serif;font-weight:300;font-size:9px;line-height:17px;padding-left:3px}
.product.featured .panel{position:absolute;left:0;top:32px;width:100%;height:65px;background:var(--red);color:#fff;text-align:center}
.product.featured h4{font-family:"Oswald",sans-serif;font-weight:300;font-size:9px;margin-top:6px}
.product.featured p{font-size:4.5px;line-height:6px;margin:4px 6px 0}

.blog-date{left:155px;top:955px;text-align:center;color:var(--red);width:30px}
.blog-date .day{font-family:"Oswald",sans-serif;font-size:20px;line-height:1}
.blog-date .month{font-family:"Oswald",sans-serif;font-size:6px}
.blog-comment{left:155px;top:1000px;width:30px;text-align:center;color:var(--red);font-family:"Oswald",sans-serif;font-size:6px}
.blog-photo{left:187px;top:929px;width:201px;height:125px;background:linear-gradient(135deg,#9aa3ab,#c9d8e6 45%,#7c98b6 70%,#d8dde2)}
.blog-body{left:393px;top:928px;width:190px}
.blog-body h3{font-family:"Oswald",sans-serif;font-weight:300;font-size:21px;color:var(--red);line-height:1.2}
.blog-body p{font-size:5px;line-height:6.5px;color:#444;margin-top:4px}
.read-more{left:395px;top:1015px;width:58px;height:13px;background:var(--red);border-radius:7px;color:#fff;font-family:"Oswald",sans-serif;font-size:6px;text-align:center;line-height:13px}
.dots{left:359px;top:1062px;display:flex;gap:3px}
.dots span{width:6px;height:6px;border:1px solid var(--red);border-radius:50%}
.dots .on{background:var(--red)}

.footer{left:0;top:1074px;width:738px;height:104px;background:var(--black);color:#fff}
.footer h5{font-family:"Oswald",sans-serif;font-weight:300;font-size:11px;color:var(--red);position:absolute;top:10px}
.footer .divider{position:absolute;top:22px;width:1px;height:68px;background:#333}
.footer-links{position:absolute;left:155px;top:33px;list-style:none;font-size:5px;line-height:7px;color:#888}
.footer-links li:first-child{color:var(--red)}
.news{position:absolute;left:277px;width:100px;font-size:4.5px;line-height:5.5px;font-weight:600}
.news small{display:block;font-weight:400;color:#ccc;font-size:3.6px;margin-top:1px}
.news small::before{content:"";display:inline-block;width:3px;height:3px;border:0.6px solid var(--red);border-radius:50%;margin-right:2px;vertical-align:middle}
.sub-label{position:absolute;left:448px;top:36px;font-size:5px;font-weight:600}
.sub-input{position:absolute;left:448px;top:45px;width:137px;height:10px;background:#444;font-size:3.8px;color:#bbb;line-height:10px;padding-left:3px}
.sub-btn{position:absolute;left:483px;top:62px;width:51px;height:12px;background:var(--red);border-radius:6px;font-family:"Oswald",sans-serif;font-size:6.5px;text-align:center;line-height:12px}
.copyright{left:0;top:1178px;width:738px;height:22px;background:var(--red);color:#fff;font-size:4.8px;text-align:center;line-height:22px}
</style>
</head>
<body>

<div class="abs topbar">
  <span class="note">We have been helping east and west transact in the most enjoyable and profitable manner since 2009!</span>
  <span class="account"><span>Sign In</span><span>Sign Up</span></span>
</div>

<header class="abs header">
  <div class="brand"><span class="mark"></span><span class="name">MERIDANE</span></div>
  <span class="brand-tag">Help East and West Transact</span>
  <nav class="nav">
    <span class="active">Home</span><span>Services</span><span>Products</span><span>Blog</span><span>About us</span><span>Join us</span><span>Help &amp;Support</span>
  </nav>
  <div class="social" aria-label="Social links"><span></span><span></span><span></span><span></span></div>
</header>

<section class="abs hero" role="img" aria-label="Smiling consultant in glasses in a bright office"></section>
<div class="abs hero-panel">
  <h2>Brief introduction of six major services:</h2>
  <ul>
    <li>+ Import &amp; Export</li><li>+ Sourcing</li>
    <li>+ Legal Service</li><li>+ Business Development</li>
    <li>+ Translation</li><li>+ Market Research</li>
  </ul>
</div>

<h2 class="section-title t-why" style="top:285px">Why Us</h2>
<ul class="abs why-list">
  <li>One stop service package to boost your business in China and globally</li>
  <li>Experts in a variety of industries ready to help</li>
  <li>Professional and cost effective service</li>
  <li>Take care of your business carefully as if they are our own business</li>
</ul>
<svg class="abs why-art" width="175" height="90" viewBox="0 0 175 90" role="img" aria-label="Diamond collage of office staff at work">
  <polygon points="0,45 45,0 90,45 45,90" fill="#b9c9d8"/>
  <polygon points="45,0 130,0 175,45 130,90 45,90 90,45" fill="#8fa9c2"/>
  <polygon points="90,45 130,0 175,45 130,90" fill="#d3dbe3"/>
</svg>

<h2 class="section-title t-services" style="top:385px">Services</h2>
<div class="card" style="left:4px;width:167px">
  <div class="photo" role="img" aria-label="Businessman facing large financial charts" style="background:linear-gradient(135deg,#f2f4f6,#dfe6ee 60%,#b7c6d8)"></div>
  <div class="label"><svg width="20" height="14" viewBox="0 0 20 14"><path d="M1 13h18M2 11l5-5 4 3 7-7" fill="none" stroke="#fff" stroke-width="2"/></svg>Business Development</div>
</div>
<div class="card featured" style="left:185px;width:169px">
  <h3><svg width="14" height="14" viewBox="0 0 14 14"><path d="M1 6h3v7H1zM4 6l3-5c1 0 2 1 1.5 3L8 6h4.5c1 0 1.5 1 1 2l-1.5 4.5c-.3.5-.8.5-1.2.5H4" fill="none" stroke="#fff" stroke-width="1.2"/></svg>Import &amp; Export</h3>
  <p>Our talented legal professionals are well equipped to deal with all the regulatory work your business requires.</p>
</div>
<div class="card" style="left:382px;width:168px">
  <div class="photo" role="img" aria-label="Hand touching glowing gear icons" style="background:radial-gradient(circle at 50% 40%,#e8f1fb,#8fb1d6 60%,#b8c7d9)"></div>
  <div class="label"><svg width="14" height="14" viewBox="0 0 14 14"><path d="M2 12l7-7 2 2-7 7H2zM9 5l2-3 2 2-3 2" fill="#fff"/></svg>Sourcing &amp; Purchasing</div>
</div>
<div class="card" style="left:566px;width:168px">
  <div class="photo" role="img" aria-label="Judge's gavel resting on an open book" style="background:linear-gradient(180deg,#e6dcd2,#cbb9a7 55%,#8a6a52)"></div>
  <div class="label"><svg width="14" height="14" viewBox="0 0 14 14"><path d="M13 1C9 1 6 3 4 7l3 3c4-2 6-5 6-9zM4 7L1 8l2 1M7 10L6 13l-1-2M3 11l-2 2" fill="#fff"/></svg>Legal Service</div>
</div>

<section class="abs order" role="img" aria-label="Dimmed photo of hands at a laptop with a coffee cup">
  <h2>Order For Recurring Services</h2>
  <div class="field" style="left:217px;top:60px;width:96px">Name :</div>
  <div class="field" style="left:321px;top:60px;width:96px">Email :</div>
  <div class="field select" style="left:425px;top:60px;width:96px">Service :</div>
  <div class="field" style="left:217px;top:94px;width:304px">Message :</div>
  <div class="send-btn">SEND</div>
</section>

<h2 class="section-title t-products" style="top:764px">Products</h2>
<div class="product" style="left:153px">
  <div role="img" aria-label="Gavel beside a laptop keyboard" style="position:absolute;inset:0;background:linear-gradient(135deg,#cfd0d0,#8c8a86 60%,#b49a6a)"></div>
  <div class="label">E-books</div>
</div>
<div class="product featured" style="left:298px">
  <div role="img" aria-label="Tablet showing charts on a desk" style="position:absolute;inset:0;background:linear-gradient(135deg,#eef0f2,#cfd6de)"></div>
  <div class="panel">
    <h4>Videos</h4>
    <p>Lorem Ipsum is simply dummy text of the printing and typesetting industry. Lorem Ipsum has been the industry's standard dummy text ever since the 1500s, when an</p>
    <svg width="8" height="8" viewBox="0 0 8 8" style="margin-top:2px"><path d="M4 0v5M2 3l2 2 2-2M1 7h6" stroke="#fff" fill="none"/></svg>
  </div>
</div>
<div class="product" style="left:444px">
  <div role="img" aria-label="Desk with calculator, coffee cup and reports" style="position:absolute;inset:0;background:linear-gradient(135deg,#e8e6e1,#f4f3ef 50%,#c9cf8a)"></div>
  <div class="label">Reports</div>
</div>

<h2 class="section-title t-blog" style="top:898px">Blog</h2>
<div class="abs blog-date"><div class="day">14</div><div class="month">March 2016</div></div>
<div class="abs blog-comment">
  <svg width="18" height="14" viewBox="0 0 18 14"><path d="M9 1C4.5 1 1 3.5 1 6.5c0 1.6 1 3 2.6 4L3 13l3.5-2c.8.2 1.6.3 2.5.3 4.5 0 8-2.5 8-5.5S13.5 1 9 1z" fill="none" stroke="#ea3345" stroke-width="1.2"/></svg>
  <div>Comment</div>
</div>
<div class="abs blog-photo" role="img" aria-label="Office windows with overlaid business charts"></div>
<article class="abs blog-body">
  <h3>General Introduction</h3>
  <p>Lorem Ipsum is simply dummy text of the printing and typesetting industry. Lorem Ipsum has been the industry's standard dummy text ever since the 1500s, when an unknown printer took a galley of type and scrambled it to make a type specimen book. It has survived not only five centuries, but also the leap into electronic typesetting, remaining essentially unchanged. It was popularised in the 1960s with the release of Letraset sheets containing Lorem Ipsum passages.</p>
</article>
<div class="abs read-more">Read more</div>
<div class="abs dots"><span></span><span class="on"></span><span></span></div>

<footer class="abs footer">
  <h5 style="left:154px">LINKS</h5>
  <ul class="footer-links"><li>Home</li><li>Services</li><li>Products</li><li>Blog</li><li>About us</li><li>Join us</li><li>Help &amp;Support</li></ul>
  <span class="divider" style="left:218px"></span>
  <h5 style="left:277px">LATEST NEWS</h5>
  <div class="news" style="top:35px">Lorem Ipsum is simply dummy text of the printing and typesetting industry.<small>14 March 2014</small></div>
  <div class="news" style="top:58px">Lorem Ipsum is simply dummy text of the printing and typesetting industry.<small>14 March 2014</small></div>
  <span class="divider" style="left:412px"></span>
  <h5 style="left:448px">SUBSCRIBE</h5>
  <div class="sub-label">Get latest updates :</div>
  <div class="sub-input">Enter E-mail</div>
  <div class="sub-btn">SEND</div>
</footer>
<div class="abs copyright">Copyright 2009 - 2016 MERIDANE &nbsp;|&nbsp; All Rights Reserved</div>

</body>
</html>
```